new construction company branding

branding

Can I have a banner made so I can hang it as 1) branding my jobsite 2) advertisement

Target Market(s)

Commercial

Industry/Entity Type

Construction Trade

Font styles to use
Other font styles liked:
• Cinzel bold

Colors
EB3D1F
EC4F4E
F09395
F8D3D4
FCEDEE

Requirements
Must have
• Bright colors for advertisement
Nice to have
• 36”x48” canvas
Should not have
• To busy

```html
<!DOCTYPE html>
<html lang="en">
<head>
<meta charset="utf-8">
<title>Keystone Build Co — Jobsite Banner</title>
<link href="https://fonts.googleapis.com/css2?family=Bebas+Neue&family=Cinzel:wght@700&family=Montserrat:wght@500;600;700&display=swap" rel="stylesheet">
<style>
  :root {
    --red: #e30d12;
    --ink: #1e1e1e;
    --white: #ffffff;
    --sky: #3f8fd0;
    --sky-light: #cfe3f3;
    --timber: #d8b98a;
  }
  html, body { margin: 0; padding: 0; overflow: hidden; background: var(--white); }
  .banner {
    position: relative;
    width: 1200px;
    height: 720px;
    overflow: hidden;
    background: var(--white);
    font-family: "Montserrat", sans-serif;
  }
  .banner__art { position: absolute; inset: 0; }
  .headline {
    position: absolute;
    left: 31px;
    top: 30px;
    margin: 0;
    font-family: "Bebas Neue", "Oswald", sans-serif;
    font-weight: 400;
    font-size: 134px;
    line-height: 1;
    color: var(--red);
    letter-spacing: 0;
    white-space: nowrap;
  }
  .subhead {
    position: absolute;
    left: 31px;
    top: 155px;
    margin: 0;
    font-weight: 500;
    font-size: 78px;
    line-height: 1;
    color: var(--ink);
    letter-spacing: 2px;
    white-space: nowrap;
  }
  .trade {
    position: absolute;
    left: 25px;
    top: 298px;
    margin: 0;
    font-weight: 500;
    font-size: 44px;
    line-height: 1;
    color: var(--ink);
    letter-spacing: 1.5px;
    white-space: nowrap;
  }
  .credentials {
    position: absolute;
    left: 25px;
    top: 356px;
    margin: 0;
    font-weight: 500;
    font-size: 31px;
    line-height: 42px;
    color: var(--red);
  }
  .phone {
    position: absolute;
    left: 61px;
    top: 580px;
    margin: 0;
    font-weight: 700;
    font-size: 66px;
    line-height: 1;
    color: var(--white);
    letter-spacing: 0.5px;
    white-space: nowrap;
  }
  .website {
    position: absolute;
    left: 49px;
    top: 664px;
    margin: 0;
    font-weight: 500;
    font-size: 22px;
    line-height: 1;
    color: var(--white);
    letter-spacing: 0.5px;
  }
  .brand {
    position: absolute;
    left: 700px;
    width: 500px;
    top: 592px;
    text-align: center;
  }
  .brand__name {
    margin: 0;
    font-family: "Cinzel", serif;
    font-weight: 700;
    font-size: 30px;
    line-height: 1;
    color: var(--white);
    white-space: nowrap;
  }
  .brand__tagline {
    margin: 14px 0 0;
    font-family: "Cinzel", serif;
    font-weight: 700;
    font-size: 23px;
    line-height: 1;
    letter-spacing: 6px;
    color: var(--red);
    white-space: nowrap;
  }
</style>
</head>
<body>
<main class="banner">
  <svg class="banner__art" width="1200" height="720" viewBox="0 0 1200 720" aria-hidden="false">
    <defs>
      <linearGradient id="sky-fade" x1="0" y1="0" x2="1" y2="0">
        <stop offset="0" stop-color="#ffffff"/>
        <stop offset="0.35" stop-color="#e6f0f8"/>
        <stop offset="0.7" stop-color="#8cbbe2"/>
        <stop offset="1" stop-color="#3f8fd0"/>
      </linearGradient>
      <linearGradient id="timber-fade" x1="0" y1="0" x2="1" y2="0">
        <stop offset="0" stop-color="#ffffff" stop-opacity="0"/>
        <stop offset="0.45" stop-color="#e8d2ad" stop-opacity="0.6"/>
        <stop offset="1" stop-color="#d2ae78" stop-opacity="0.9"/>
      </linearGradient>
    </defs>

    <g class="photo" role="img" aria-label="Photo of a timber-framed house under construction against a blue sky">
      <rect x="560" y="0" width="640" height="440" fill="url(#sky-fade)"/>
      <path d="M760 440 L1000 150 L1200 120 L1200 440 Z" fill="url(#timber-fade)"/>
    </g>

    <!-- divider under headline -->
    <line class="divider" x1="33" y1="263" x2="628" y2="263" stroke="var(--red)" stroke-width="1.5"/>
    <polygon class="divider__accent" points="327,244 396,244 367,276 299,276" fill="var(--ink)"/>

    <!-- red house outline -->
    <path class="house" fill="var(--red)"
      d="M547 425 Q547 421 551 421 L603 421 Q607 421 607 425 L607 518 L798 340 L887 424 L840 461 L796 421 L498 720 L413 720 L606 530 L606 576 L547 576 Z"/>
    <rect class="phone-band" x="0" y="576" width="560" height="77" fill="var(--red)"/>
    <polygon class="web-band" points="0,655 387,655 346,702 0,702" fill="var(--ink)"/>

    <!-- crescent sweep -->
    <path class="sweep" fill="var(--red)"
      d="M776 513 C700 530 640 600 636 700 L644 702 C660 620 700 565 752 540 C740 535 760 520 776 513 Z"/>

    <!-- dark brand panel with white rim -->
    <path class="panel__rim" fill="var(--white)" d="M620 720 Q790 380 1200 340 L1200 720 Z"/>
    <path class="panel" fill="var(--ink)" d="M636 720 Q810 400 1200 351 L1200 720 Z"/>

    <!-- phone icon -->
    <g class="icon-phone" fill="none" stroke="var(--white)" stroke-width="2.5">
      <rect x="26" y="591" width="22" height="46" rx="4"/>
      <line x1="33" y1="597" x2="41" y2="597"/>
      <line x1="34" y1="631" x2="40" y2="631"/>
    </g>
    <!-- globe icon -->
    <g class="icon-globe" fill="none" stroke="var(--white)" stroke-width="1.4">
      <circle cx="30" cy="676" r="8"/>
      <ellipse cx="30" cy="676" rx="3.5" ry="8"/>
      <line x1="22" y1="676" x2="38" y2="676"/>
      <line x1="24" y1="671" x2="36" y2="671"/>
      <line x1="24" y1="681" x2="36" y2="681"/>
    </g>
  </svg>

  <h1 class="headline">Together Achieving</h1>
  <p class="subhead">COMMAN GOALS</p>
  <p class="trade">GENERAL CONTRACTOR</p>
  <p class="credentials">License b no #2048736<br>Bonded/insured</p>
  <p class="phone">123-4567-890</p>
  <p class="website">www.yourwebsiet.com</p>

  <div class="brand">
    <p class="brand__name">KEYSTONE BUILD CO LLC</p>
    <p class="brand__tagline">General Contractor</p>
  </div>
</main>
</body>
</html>
```